Website for business consultancy - bright and happy feel needed

I need a website with 3/4 pages. I want the first page designed first and the rest will be easy. I need some pictures but none with corporate looking people. I need links to chatterbox and careerweb. I need a contact form. I have samples of websites i like, fonts i like and I need a small logo also. I like simple, clean lines and I want a bright, happy and feminine feel. My audience are small businesses so I don't want them intimidated by new much of a corporate feel.
Updates

Project Deadline Extended Reason: I have not received a design that reflects what I believe the brief to be, therefore I am extending the deadline and increasing the amount to be paid. Added Thursday, October 13, 2016

Target Market(s)

Small medium size businesses who want to grow and need that help but they cannot afford a full time financial director.

Industry/Entity Type

Business Consultant

Number of Pages Required

4 page

Font styles to use
Other font styles liked:
• i can attach images

Colors
fcf0f6
e667a6
85cae6
ffffff
fbee3e

Requirements
Must have
• Link to chatterbox and career web
• Contact form linked to my email
• Pictures - full width images where required
• Colour
• Mobile ready
• Soft feminine feel to it
• I dont want it to look like a corporate business consultancy - much more marketing or interior deign feel
Nice to have
• I would like the 3 services I have in 3 boxes that you click and takes you to a place with more information on the service.
• pictures thinking outside of the box
• Can be wordpress if need be
Should not have
• pictures with too much of a corporate feel
• No pictures of coporate people at all
• i like the following websites
• www.pebblordo.co.uk and others that are attached in the documents with a feminine feel to them

```html
<!DOCTYPE html>
<html lang="en">
<head>
<meta charset="utf-8">
<title>Maren Holt Consulting</title>
<link href="https://fonts.googleapis.com/css2?family=Lato:wght@400;700&family=Raleway:wght@600;700&family=Cinzel:wght@400&display=swap" rel="stylesheet">
<style>
:root{
  --ink:#2a2a2a;
  --text:#333;
  --muted:#8a8a8a;
  --pink:#e667a6;
  --pink-deep:#d4548f;
  --blush:#fcf0f6;
  --blush-edge:#f3c6dc;
  --sky:#85cae6;
  --sun:#fbee3e;
  --white:#fff;
}
*{margin:0;padding:0;box-sizing:border-box}
html,body{width:1026px;height:1200px;overflow:hidden;background:var(--white)}
body{position:relative;font-family:'Lato',sans-serif;color:var(--text)}
.abs{position:absolute}

/* header */
.brand{left:87px;top:22px;display:flex;align-items:center;gap:12px}
.brand-dot{width:46px;height:46px;border-radius:50%;background:var(--pink)}
.brand-name{display:block;font-family:'Raleway',sans-serif;font-weight:700;font-size:29px;color:var(--ink);line-height:1}
.brand-tag{display:block;font-family:'Cinzel',serif;font-size:12px;letter-spacing:8px;color:var(--ink);margin-top:4px;padding-left:18px}
.nav{top:20px;left:0;width:1026px;height:60px}
.nav-item{position:absolute;top:0;transform:translateX(-50%);text-align:center;font-size:12.5px;color:var(--muted);white-space:nowrap}
.nav-item svg{display:block;margin:0 auto 6px;height:24px}
.nav-item.is-active{color:var(--pink-deep);font-weight:700}

/* hero */
.hero{left:0;top:89px;width:1026px;height:403px;background:linear-gradient(90deg,#fbe6ef 0%,var(--blush) 35%,#f4f0f6 65%,#e6eef3 100%)}
.hero-rail{left:0;top:340px;width:1026px;height:14px;background:linear-gradient(90deg,#f6c9a0,#f3cdb0 60%,#efd6c2)}
.hero-person{left:640px;top:89px;width:300px;height:375px;background:linear-gradient(180deg,#e3c6b2,#d2b9a6 60%,#e2d3c8)}
.hero-title{left:88px;top:196px;font-family:'Raleway',sans-serif;font-weight:700;font-size:35px;line-height:46px;color:var(--ink)}
.hero-dots{left:88px;top:376px;display:flex;gap:5px}
.hero-dots span{width:9px;height:9px;border-radius:50%;background:var(--blush-edge)}
.hero-dots span.is-current{background:var(--pink)}

.social{right:0;width:40px;height:36px;color:var(--white);font-size:6.5px;font-weight:700;display:flex;align-items:center;justify-content:center;text-align:center;white-space:nowrap}
.social-careerweb{top:236px;background:var(--pink)}
.social-chatterbox{top:275px;background:var(--sky)}

/* services */
.services-back{left:83px;top:464px;width:859px;height:30px;background:var(--white)}
.service{top:472px;width:260px;height:304px;background:var(--blush);border:3px solid var(--blush-edge);text-align:center}
.service::after{content:"";position:absolute;inset:3px;border:1px solid var(--white);pointer-events:none}
.service-photo{margin:3px 3px 0;height:135px}
.service-title{font-weight:700;font-size:14px;color:#111;margin-top:18px}
.service-body{font-size:12px;line-height:17.5px;color:#444;margin:12px 10px 0}
.service-btn{display:inline-block;margin-top:14px;background:var(--pink);color:var(--white);font-weight:700;font-size:12px;padding:4px 13px;border-radius:12px}

/* about */
.about-photo{left:88px;top:815px;width:228px;height:349px;background:linear-gradient(180deg,var(--white) 0%,#f1d9c6 25%,#3a3440 55%,#2a2630 100%);border-radius:110px 110px 0 0}
.about-copy{left:357px;top:840px;width:579px;font-size:13px;line-height:17.2px;letter-spacing:.15px;color:#222}
.about-copy p{margin-bottom:13px}
.checklist{list-style:none;margin-top:16px}
.checklist li{display:flex;align-items:center;gap:8px;height:26px;font-size:12.5px;letter-spacing:0}

.footer{left:0;top:1164px;width:1026px;height:36px;background:var(--pink);color:var(--white);font-size:11px;display:flex;align-items:center;justify-content:center}
</style>
</head>
<body>

<header>
  <div class="brand abs">
    <span class="brand-dot"></span>
    <div>
      <span class="brand-name">Maren Holt</span>
      <span class="brand-tag">CONSULTING</span>
    </div>
  </div>
  <nav class="nav abs">
    <div class="nav-item is-active" style="left:503px">
      <svg viewBox="0 0 24 24" width="24"><path d="M2 12 12 3l10 9h-3v9h-5v-6h-4v6H5v-9z" fill="#e667a6"/></svg>Home</div>
    <div class="nav-item" style="left:589px">
      <svg viewBox="0 0 32 24" width="32"><ellipse cx="13" cy="10" rx="11" ry="8" fill="#999"/><path d="M5 15l-2 6 7-4z" fill="#999"/><ellipse cx="22" cy="13" rx="9" ry="6.5" fill="#aaa"/></svg>Mentoring</div>
    <div class="nav-item" style="left:680px">
      <svg viewBox="0 0 24 24" width="24"><path d="M9 3h6l-2 4h-2z" fill="#999"/><circle cx="12" cy="15" r="8" fill="#999"/><text x="12" y="19" font-size="10" fill="#fff" text-anchor="middle" font-family="Lato,sans-serif">$</text></svg>Finance</div>
    <div class="nav-item" style="left:789px">
      <svg viewBox="0 0 24 24" width="24"><rect x="3" y="14" width="4" height="8" fill="#999"/><rect x="9" y="11" width="4" height="11" fill="#999"/><rect x="15" y="8" width="4" height="14" fill="#999"/><path d="M3 11l6-4 4 3 7-7" stroke="#999" stroke-width="2" fill="none"/></svg>Business Seeking</div>
    <div class="nav-item" style="left:907px">
      <svg viewBox="0 0 24 24" width="24"><path d="M7 2l3 5-2 2c1 3 3 6 6 8l2-2 5 3-2 4C10 21 3 12 4 4z" fill="#999"/></svg>Contact Us</div>
  </nav>
</header>

<section>
  <div class="hero abs" role="img" aria-label="Bright office interior with glass railing"></div>
  <div class="hero-rail abs"></div>
  <div class="hero-person abs" role="img" aria-label="Smiling consultant in a beige suit leaning on a railing"></div>
  <h1 class="hero-title abs">Not All Business Can<br>Afford A Few Time<br>Financial Director</h1>
  <div class="hero-dots abs"><span class="is-current"></span><span></span><span></span><span></span></div>
  <a class="social social-careerweb abs">careerweb</a>
  <a class="social social-chatterbox abs">chatterbox</a>
</section>

<section>
  <div class="services-back abs"></div>
  <article class="service abs" style="left:90px">
    <div class="service-photo" role="img" aria-label="Two colleagues reviewing a tablet" style="background:linear-gradient(90deg,#e9a07a 0%,#f7ece6 30%,#8d8796 70%,#eee 100%)"></div>
    <h3 class="service-title">Business Coach &amp; Mentor</h3>
    <p class="service-body">Ut wisi enim ad minim veniam, quisl mor nostrni exerci tation ullamcorper suskcipit no lobortis norl nislk ut aliquip.</p>
    <span class="service-btn">Read More</span>
  </article>
  <article class="service abs" style="left:383px">
    <div class="service-photo" role="img" aria-label="Hand with pen over a printed bar chart" style="background:linear-gradient(135deg,#f0cdb9 0%,#f8f4f1 45%,#85cae6 75%,#eef2f5 100%)"></div>
    <h3 class="service-title">Leasing Finance Reworking</h3>
    <p class="service-body">Ut wisi enim ad minim veniam, quisl mor nostrni exerci tation ullamcorper suskcipit no lobortis norl nislk ut aliquip.</p>
    <span class="service-btn">Read More</span>
  </article>
  <article class="service abs" style="left:676px">
    <div class="service-photo" role="img" aria-label="Sketch of a man drawing a rising bar chart" style="background:linear-gradient(90deg,#eeeeee 0%,#d6d6d6 60%,#9a9a9a 100%)"></div>
    <h3 class="service-title">Taking your Business to next Level</h3>
    <p class="service-body">Ut wisi enim ad minim veniam, quisl mor nostrni exerci tation ullamcorper suskcipit no lobortis norl nislk ut aliquip.</p>
    <span class="service-btn">Read More</span>
  </article>
</section>

<section>
  <div class="about-photo abs" role="img" aria-label="Consultant in a dark blazer with arms crossed"></div>
  <div class="about-copy abs">
    <p>Lorem ipsum dolor sit amet, consectetuer adipiscing elit, sed diam nonummy nibh euismod tincidunt ut laoreet dolore magna aliquam erat volutpat. Ut wisi enim ad minim veniam, quis nostrud exerci tation ullamcorper suscipit lobortis nisl ut aliquip ex ea commodo consequat. Duis autem vel eum iriure dolor in hendrerit in vulputate velit esse molestie consequat, vel illum dolore eu feugiat nulla facilisis at vero eros et accumsan et iusto odio dignissim qui blandit praesent luptatum zzril delenit augue duis dolore te feugait nulla facilisi.</p>
    <p>Lorem ipsum dolor sit amet, consectetuer adipiscing elit, sed diam nonummy nibh euismod tincidunt ut laoreet dolore magna aliquam erat volutpat. Ut wisi enim ad minim veniam, quis nostrud exerci tation ullamcorper suscipit lobortis nisl ut.</p>
    <ul class="checklist">
      <li><svg width="15" height="13" viewBox="0 0 15 13"><path d="M1 7l4 4 9-10" stroke="#e667a6" stroke-width="2" fill="none"/></svg>laoreet dolore magna aliamer at volutpat. Ut wisi enim ad minim veniam</li>
      <li><svg width="15" height="13" viewBox="0 0 15 13"><path d="M1 7l4 4 9-10" stroke="#e667a6" stroke-width="2" fill="none"/></svg>laoreet dolore magna aliamer at volutpat. Ut wisi enim</li>
      <li><svg width="15" height="13" viewBox="0 0 15 13"><path d="M1 7l4 4 9-10" stroke="#e667a6" stroke-width="2" fill="none"/></svg>laoreet dolore magna aliamer at volutpat. Ut wisi enim ad minim</li>
      <li><svg width="15" height="13" viewBox="0 0 15 13"><path d="M1 7l4 4 9-10" stroke="#e667a6" stroke-width="2" fill="none"/></svg>laoreet dolore magna aliamer at volutpat. Ut wisi enim</li>
    </ul>
  </div>
</section>

<footer class="footer abs">Copyright ©2016 Maren Holt Consultancy&nbsp; .&nbsp; All Rights Reserved.</footer>

</body>
</html>
```